Give Bright Oak an Online Presence!

Bright Oak Property Maintenance is an Australian Owned property maintenance company who needs a stand out online presence.

BOK maintains many buildings and sites and wants to appeal to a corporate professional market with their brand new website. BOK is essentially a handyman service offering all maintenance services to home owners, office managers, real estate agents and strata managers.

The Website:
We need a corporate website that appeals to our broader customer base (property owners, property managers, office managers) the copy is being written by a professional so use filler text for now.

Things that we want:
Home page that sets us apart and appeals to the corporate and residential market. The home page needs to not focus on either the residential or commercial market. The home page should focus on our logo and branding. We have a logo already and it is attached to the brief, please use it and try to consider the colour pallette that goes with it. Whilst we want the site to appear strong and manly it is important to remember that 95% of our customers are female so we need the site to be appealing to women. Women need to believe that we are strong, dependable and trustworthy.
We'd like a quote page and potentially also the ability to get a quote from the home page (please don't put it in if it ruins the overall feel of the home page)
An "about us" page
A contact us page
A blog that's built in (we don't want to link to an external blog)
(overall we'd expect to have 6 or 7 pages total)

The site will also need coding - we expect this to be done in a separate project but need you to consider a few things about the coding side of things.

It needs to be iPhone and iPad compatible.

We'd like you to suggest the best CMS that you would use or if you would suggest not using a CMS please let us know with your submissions.

Target Market(s)

Property owners, office managers and property managers who need maintenance on buildings (So all of them)

Industry/Entity Type

Property Maintenance

Requirements
Must have
• Our Logo
Home page
About Us
Residential
Commercial
Real Estate/Strata
Contact Us/Quote
Blog
Nice to have
• Quote form included in home page
Movement on the home page at least
Should not have
• other logos, too much colour
NO FLASH

```html
<!DOCTYPE html>
<html lang="en">
<head>
<meta charset="utf-8">
<title>Bright Oak Property Maintenance</title>
<link rel="stylesheet" href="https://fonts.googleapis.com/css2?family=Open+Sans:ital,wght@0,400;0,600;0,700;1,400&family=Ubuntu:wght@700&display=swap">
<style>
  :root {
    --canvas: #3a3b3d;
    --orange: #c2580f;
    --orange-box: #d9722b;
    --orange-text: #cc5c12;
    --page: #f1f1f1;
    --page-band: #e9e9e9;
    --rule: #dcdcdc;
    --ribbon: #262626;
    --ribbon-dark: #121212;
    --ink: #222;
    --muted: #8a8a8a;
    --grey-head: #6f6f6f;
    --footer: #2c2c2c;
    --footer-bottom: #252525;
    --field: #3b3b3b;
    --green: #5aa52a;
    --white: #ffffff;
  }
  * { box-sizing: border-box; margin: 0; padding: 0; }
  html, body { width: 1200px; height: 2657px; overflow: hidden; }
  body {
    background: var(--canvas);
    font-family: "Open Sans", Arial, sans-serif;
    color: var(--ink);
    position: relative;
  }
  .site {
    position: absolute; left: 150px; top: 49px; width: 900px; height: 2533px;
    background: var(--page);
    border-radius: 6px 6px 0 0;
  }

  /* Header */
  .masthead {
    position: absolute; left: 0; top: 0; width: 900px; height: 551px;
    background: var(--orange); border-radius: 6px 6px 0 0;
  }
  .slider-arrow {
    position: absolute; top: 210px; font-size: 58px; font-weight: 700;
    color: var(--ribbon-dark); line-height: 1;
  }
  .slider-arrow.prev { left: 50px; }
  .slider-arrow.next { right: 50px; }
  .brand {
    position: absolute; left: 250px; top: 70px; width: 400px; height: 360px;
    display: flex; flex-direction: column; align-items: center; justify-content: center; gap: 22px;
  }
  .brand-mark { width: 70px; height: 70px; background: var(--ribbon-dark); border-radius: 50%; }
  .brand-name {
    font-family: "Open Sans", Arial, sans-serif; font-weight: 700; font-size: 40px;
    color: var(--ribbon-dark); text-align: center; line-height: 1.15;
  }
  .ribbon {
    position: absolute; left: -17px; top: 423px; width: 934px; height: 60px;
    background: linear-gradient(var(--ribbon), var(--ribbon-dark));
    display: flex; align-items: center; justify-content: center; gap: 20px;
    box-shadow: 0 4px 8px rgba(0,0,0,.35);
  }
  .ribbon-fold { position: absolute; top: 483px; }
  .ribbon-fold.left { left: -17px; }
  .ribbon-fold.right { right: -17px; }
  .ribbon-text { color: #e8e8e8; font-size: 18px; letter-spacing: -0.3px; }
  .btn-contact {
    background: var(--orange-box); color: var(--white); font-size: 15px; font-weight: 600;
    padding: 8px 20px; border-radius: 3px; border: 1px solid #e48a45;
  }

  /* Quote */
  .quote-section { position: absolute; left: 0; top: 551px; width: 900px; height: 480px; border-bottom: 2px solid var(--rule); }
  .section-title {
    position: absolute; left: 45px; top: 73px;
    font-family: "Ubuntu", sans-serif; font-weight: 700; font-size: 40px; color: var(--orange-box);
    text-shadow: 1px 2px 0 #7a3a0d;
  }
  .form-slot {
    position: absolute; left: 45px; top: 140px; width: 830px; height: 302px;
    background: var(--orange-box); border: 1px solid #c65f19;
    display: flex; align-items: center; justify-content: center;
    color: var(--white); font-weight: 700; font-size: 38px; letter-spacing: .5px;
  }

  /* Services */
  .services {
    position: absolute; left: 0; top: 1031px; width: 900px; height: 430px;
    display: grid; grid-template-columns: repeat(4, 1fr); padding: 45px 15px 0 15px; row-gap: 26px;
  }
  .service { text-align: center; padding: 0 20px; }
  .service-title { color: var(--orange-text); font-weight: 700; font-size: 18px; line-height: 30px; letter-spacing: -0.3px; }
  .service-text { color: var(--muted); font-size: 12.5px; line-height: 20px; margin-top: 4px; }

  /* Testimonial */
  .testimonial {
    position: absolute; left: 0; top: 1461px; width: 900px; height: 95px;
    background: var(--page-band); border-top: 2px solid var(--rule); border-bottom: 2px solid var(--rule);
    text-align: center; padding-top: 17px;
  }
  .testimonial-quote { font-family: Arial, sans-serif; color: var(--orange-text); font-size: 24px; }
  .testimonial-cite { font-family: Arial, sans-serif; font-style: italic; font-size: 11px; color: #444; margin-top: 6px; }

  /* Video */
  .video-section { position: absolute; left: 0; top: 1556px; width: 900px; height: 408px; border-bottom: 2px solid #e3e3e3; }
  .video-copy { position: absolute; left: 20px; top: 106px; width: 290px; }
  .video-title { color: var(--orange-text); font-weight: 700; font-size: 26px; }
  .video-kicker { font-size: 11px; letter-spacing: 3px; color: var(--muted); margin-top: 8px; font-weight: 600; }
  .video-text { font-size: 11.5px; color: var(--muted); line-height: 19px; margin-top: 14px; }
  .video-frame {
    position: absolute; left: 320px; top: 45px; width: 564px; height: 318px;
    background: var(--white); border: 1px solid #cfcfcf; box-shadow: 0 3px 10px rgba(0,0,0,.45);
  }

  /* Share */
  .share { position: absolute; left: 0; top: 2044px; width: 900px; height: 92px;
    background: var(--page-band); border-top: 2px solid var(--rule); border-bottom: 3px solid var(--orange); }
  .share-title { position: absolute; left: 170px; top: 20px; color: var(--grey-head); font-weight: 700; font-size: 28px; letter-spacing: -0.5px; }

  /* Footer */
  .footer { position: absolute; left: 0; top: 2136px; width: 900px; height: 393px; background: var(--footer); }
  .footer-col { position: absolute; top: 32px; width: 270px; }
  .footer-col.contact { left: 20px; }
  .footer-col.tweets { left: 320px; }
  .footer-col.about { left: 620px; width: 265px; }
  .footer-title { color: var(--orange-text); font-weight: 700; font-size: 21px; }
  .field-label { color: #9a9a9a; font-size: 10px; margin-top: 18px; }
  .field { width: 236px; height: 28px; background: var(--field); border: 1px solid #333; margin-top: 6px; }
  .field.area { height: 92px; }
  .btn-green { display: inline-block; background: var(--green); color: var(--white); font-size: 11px; font-weight: 600;
    padding: 4px 14px; border-radius: 3px; margin-top: 16px; border: 1px solid #6ec23a; }
  .about-lead { color: #8c8c8c; font-size: 12px; font-weight: 700; line-height: 19px; margin-top: 16px; }
  .about-text { color: #7a7a7a; font-size: 10.5px; line-height: 16.5px; margin-top: 18px; }
  .footer-bottom { position: absolute; left: 0; top: 2529px; width: 900px; height: 52px; background: var(--footer-bottom); border-top: 1px solid #1f1f1f; }
  .copyright { position: absolute; left: 20px; top: 17px; color: #4a4a4a; font-size: 11px; }
</style>
</head>
<body>
  <div class="site">
    <header class="masthead">
      <span class="slider-arrow prev">&lt;</span>
      <span class="slider-arrow next">&gt;</span>
      <div class="brand">
        <span class="brand-mark"></span>
        <span class="brand-name">Bright Oak<br>Property Maintenance</span>
      </div>
      <div class="ribbon">
        <span class="ribbon-text">Get a quote in no time.</span>
        <span class="btn-contact">Contact Us</span>
      </div>
      <svg class="ribbon-fold left" width="17" height="14"><polygon points="0,0 17,0 17,14" fill="#0b0b0b"/></svg>
      <svg class="ribbon-fold right" width="17" height="14"><polygon points="0,0 17,0 0,14" fill="#0b0b0b"/></svg>
    </header>

    <section class="quote-section">
      <h2 class="section-title">Quick Quote Form</h2>
      <div class="form-slot">Form can be added here</div>
    </section>

    <section class="services">
      <div class="service"><h3 class="service-title">All Commercial And Residential Handyman Work</h3><p class="service-text">Cras justo odio, dapibus ac facilisis in, egestas eget quam. Nullam id dolor id nibh ultricies.</p></div>
      <div class="service"><h3 class="service-title">Doors And Locks</h3><p class="service-text">Cras justo odio, dapibus ac facilisis in, egestas eget quam. Nullam id dolor id nibh ultricies.</p></div>
      <div class="service"><h3 class="service-title">Strata Management Work</h3><p class="service-text">Cras justo odio, dapibus ac facilisis in, egestas eget quam. Nullam id dolor id nibh ultricies.</p></div>
      <div class="service"><h3 class="service-title">Scheduled Maintenance</h3><p class="service-text">Cras justo odio, dapibus ac facilisis in, egestas eget quam. Nullam id dolor id nibh ultricies.</p></div>
      <div class="service"><h3 class="service-title">Lighting</h3><p class="service-text">Cras justo odio, dapibus ac facilisis in, egestas eget quam. Nullam id dolor id nibh ultricies.</p></div>
      <div class="service"><h3 class="service-title">Pictures And Whiteboards Hung</h3><p class="service-text">Cras justo odio, dapibus ac facilisis in, egestas eget quam. Nullam id dolor id nibh ultricies.</p></div>
      <div class="service"><h3 class="service-title">Windows And Screens</h3><p class="service-text">Cras justo odio, dapibus ac facilisis in, egestas eget quam. Nullam id dolor id nibh ultricies.</p></div>
      <div class="service"><h3 class="service-title">All Repairs</h3><p class="service-text">Cras justo odio, dapibus ac facilisis in, egestas eget quam. Nullam id dolor id nibh ultricies.</p></div>
    </section>

    <section class="testimonial">
      <p class="testimonial-quote">“Easily setup, and great service. Awesome.”</p>
      <p class="testimonial-cite">— Anna Reed, samplesite.com</p>
    </section>

    <section class="video-section">
      <div class="video-copy">
        <h3 class="video-title">View a video tutorial →</h3>
        <p class="video-kicker">FAST AND EASY</p>
        <p class="video-text">Cras justo odio, dapibus ac facilisis in, egestas eget quam. Nullam id dolor id nibh ultricies. Cras justo odio, dapibus ac facilisis in, egestas eget quam. Nullam id dolor id nibh ultricies.</p>
      </div>
      <div class="video-frame" role="img" aria-label="Video player area"></div>
    </section>

    <section class="share">
      <h3 class="share-title">Spread the good word →</h3>
    </section>

    <footer class="footer">
      <div class="footer-col contact">
        <h4 class="footer-title">Drop us a line</h4>
        <p class="field-label">Name</p><div class="field"></div>
        <p class="field-label">E-mail</p><div class="field"></div>
        <p class="field-label">Message</p><div class="field area"></div>
        <span class="btn-green">Send</span>
      </div>
      <div class="footer-col tweets">
        <h4 class="footer-title">Latest tweets</h4>
      </div>
      <div class="footer-col about">
        <h4 class="footer-title">About</h4>
        <p class="about-lead">Cras justo odio, dapibus ac facilisis in, egestas eget quam.</p>
        <p class="about-text">Nullam id dolor id nibh ultricies. Cras justo odio, dapibus ac facilisis in, egestas eget quam. Nullam id dolor id nibh ultricies. Cras justo odio, dapibus ac facilisis in, egestas eget quam. Nullam id dolor id nibh ultricies. Cras justo odio, dapibus ac facilisis in, egestas eget quam. Nullam id dolor id nibh ultricies. Cras justo odio, dapibus ac facilisis in, egestas eget quam. Nullam id dolor id nibh ultricies. Cras justo odio, dapibus ac facilisis in, egestas eget quam. Nullam id dolor id nibh ultricies. Cras justo odio, dapibus ac facilisis in, egestas eget quam.</p>
        <span class="btn-green">Read More</span>
      </div>
    </footer>
    <div class="footer-bottom"><p class="copyright">Bright Oak © 2012</p></div>
  </div>
</body>
</html>
```